Design a business Card

Design a business card (front and back) for a Technology Consulting firm. Preference is for a clean look - professional, favour minimalist rather than something busy. two logos are attached. You can use any of them. . The information below is for the purpose of presenting an entry in the contest, but the winner will be given correct information to product another version of the entry. The winner will also be given an opportunity to prepare a letterhead (ideally consistent with the business card).

Carla Wendover
Partner
+61 438 926 417
+61 7 3890 2615
jane@[url removed, login to view]
[url removed, login to view]
GPO Box 6093
Brisbane QLD 4009

The winning entry should be in a format that most business card printers can easily print.

```html
<!DOCTYPE html>
<html lang="en">
<head>
<meta charset="utf-8">
<title>Halvern Consulting Services – Business Card</title>
<link href="https://fonts.googleapis.com/css2?family=Roboto:wght@400;500;700&family=Roboto+Condensed:wght@400;700&display=swap" rel="stylesheet">
<style>
  :root {
    --stage: #3a3b3e;
    --card: #2b2c2f;
    --red: #c8191f;
    --grey: #a3a4a7;
    --grey-dim: #7d7e82;
    --icon-glyph: #2b2c2f;
  }
  * { box-sizing: border-box; margin: 0; padding: 0; }
  html, body {
    width: 1200px; height: 900px; overflow: hidden;
    background: var(--stage);
    font-family: "Roboto", Arial, sans-serif;
  }
  .stage {
    position: relative; width: 1200px; height: 900px;
    display: flex; align-items: center; justify-content: center; gap: 40px;
  }
  .card {
    position: relative; width: 540px; height: 309px;
    background: var(--card);
    box-shadow: 0 10px 30px rgba(0,0,0,.35);
  }
  .corner { position: absolute; width: 22px; height: 22px; background: var(--red); }
  .corner--tl { top: 0; left: 0; }
  .corner--tr { top: 0; right: 0; }
  .corner--bl { bottom: 0; left: 0; }
  .corner--br { bottom: 0; right: 0; }

  /* brand lockup */
  .brand { display: flex; align-items: center; gap: 10px; }
  .brand__name {
    font-family: "Roboto", Arial, sans-serif;
    font-weight: 700; color: var(--red);
    font-size: 28px; letter-spacing: 1px; line-height: 1;
  }
  .brand__divider { width: 1px; height: 42px; background: var(--grey-dim); }
  .brand__text { color: var(--grey); }
  .brand__company {
    font-family: "Roboto Condensed", "Arial Narrow", sans-serif;
    font-weight: 700; font-size: 13px; line-height: 1.05; text-transform: uppercase;
  }
  .brand__tagline {
    margin-top: 4px; padding-bottom: 3px;
    font-size: 6px; letter-spacing: 1.2px; text-transform: uppercase;
    color: var(--grey-dim);
    border-bottom: 1px solid var(--grey-dim);
    width: 130px;
  }

  .card--back { display: flex; align-items: center; justify-content: center; }
  .card--back .brand__name { font-size: 40px; }
  .card--back .brand__divider { height: 48px; }
  .card--back .brand__company { font-size: 18px; }
  .card--back .brand__tagline { font-size: 7.5px; width: 170px; }

  /* contact side */
  .card--front .brand { position: absolute; right: 40px; top: 150px; }
  .person { position: absolute; left: 48px; top: 42px; }
  .person__name {
    font-size: 17px; font-weight: 500; letter-spacing: .5px; text-transform: uppercase;
    color: var(--grey);
  }
  .person__name .surname { color: var(--red); }
  .person__role {
    margin-top: 3px; font-size: 10px; letter-spacing: 1.5px; text-transform: uppercase; color: var(--grey-dim);
  }
  .contacts { position: absolute; left: 48px; top: 104px; display: grid; gap: 12px; }
  .contacts--secondary { left: 48px; top: 222px; grid-template-columns: auto auto; column-gap: 36px; }
  .contact { display: flex; align-items: center; gap: 9px; font-size: 11.5px; color: var(--grey); }
  .contact__icon {
    width: 18px; height: 18px; border-radius: 3px; background: var(--red);
    display: flex; align-items: center; justify-content: center; flex: none;
  }
  .contact__icon svg { width: 11px; height: 11px; fill: var(--icon-glyph); }
</style>
</head>
<body>
<main class="stage">

  <section class="card card--front" aria-label="Business card, contact side">
    <span class="corner corner--tl"></span><span class="corner corner--tr"></span>
    <span class="corner corner--bl"></span><span class="corner corner--br"></span>

    <div class="person">
      <p class="person__name">Carla <span class="surname">Wendover</span></p>
      <p class="person__role">Partner</p>
    </div>

    <div class="contacts">
      <p class="contact">
        <span class="contact__icon"><svg viewBox="0 0 12 12"><path d="M6 0.5a4 4 0 0 0-4 4c0 3 4 7 4 7s4-4 4-7a4 4 0 0 0-4-4zm0 5.6a1.6 1.6 0 1 1 0-3.2 1.6 1.6 0 0 1 0 3.2z"/></svg></span>
        GPO Box 6093 Brisbane QLD 4009
      </p>
      <p class="contact">
        <span class="contact__icon"><svg viewBox="0 0 12 12"><path d="M2.6 1l1.8 2.3-1 1.1c.7 1.5 1.7 2.5 3.2 3.2l1.1-1L10 8.4 9 10.6C5 10.3 1.7 7 1.4 3z"/></svg></span>
        +61 438 926 417
      </p>
      <p class="contact">
        <span class="contact__icon"><svg viewBox="0 0 12 12"><path d="M1 2.5h10v7H1zM1.6 3.2L6 6.6l4.4-3.4v.9L6 7.5 1.6 4.1z"/></svg></span>
        carla@ridgeforth.com
      </p>
    </div>

    <div class="contacts contacts--secondary">
      <p class="contact">
        <span class="contact__icon"><svg viewBox="0 0 12 12"><path d="M3.5 0.5h5a.8.8 0 0 1 .8.8v9.4a.8.8 0 0 1-.8.8h-5a.8.8 0 0 1-.8-.8V1.3a.8.8 0 0 1 .8-.8zm.4 1.5v7h4.2V2zM6 9.6a.6.6 0 1 0 0 1.2.6.6 0 0 0 0-1.2z"/></svg></span>
        +61 7 3890 2615
      </p>
      <p class="contact">
        <span class="contact__icon"><svg viewBox="0 0 12 12"><path d="M6 .8a5.2 5.2 0 1 0 0 10.4A5.2 5.2 0 0 0 6 .8zm0 1.2c.6.6 1.1 1.6 1.3 3H4.7C4.9 3.6 5.4 2.6 6 2zM4.7 6h2.6c-.2 1.4-.7 2.4-1.3 3-.6-.6-1.1-1.6-1.3-3zM2 6h1.7c.1 1.1.4 2 .8 2.7A4 4 0 0 1 2 6zm0-1a4 4 0 0 1 2.5-2.7c-.4.7-.7 1.6-.8 2.7zm6.3 1H10a4 4 0 0 1-2.5 2.7c.4-.7.7-1.6.8-2.7zm0-1c-.1-1.1-.4-2-.8-2.7A4 4 0 0 1 10 5z"/></svg></span>
        http://www.ridgeforth.com
      </p>
    </div>

    <div class="brand">
      <span class="brand__name">Halvern</span>
      <span class="brand__divider"></span>
      <div class="brand__text">
        <p class="brand__company">Halvern Consulting<br>Services Ltd</p>
        <p class="brand__tagline">Advice You Can Trust</p>
      </div>
    </div>
  </section>

  <section class="card card--back" aria-label="Business card, logo side">
    <span class="corner corner--tl"></span><span class="corner corner--tr"></span>
    <span class="corner corner--bl"></span><span class="corner corner--br"></span>
    <div class="brand">
      <span class="brand__name">Halvern</span>
      <span class="brand__divider"></span>
      <div class="brand__text">
        <p class="brand__company">Halvern Consulting<br>Services Ltd</p>
        <p class="brand__tagline">Advice You Can Trust</p>
      </div>
    </div>
  </section>

</main>
</body>
</html>
```